Keelbrook Vault Holdings Needs A Website

We are looking for a website for a new company. 4 Pages

Needs to be responsive and mobile friendly for all browsers and coded for both Android & IOS. SEO is also important.

Website Brief – Keelbrook Vault Holdings
Domain: www.keelbrookvault.net
Email: info@keelbrookvault.net
Phone: to be inserted later
Address: 40837 52 Ave, Edmonton, AB T6K 3R8
Platform: WordPress (recommended for flexibility, SEO tools, and ease of editing)
Requirements:
• Responsive & mobile-friendly (Android & iOS)
• Cross-browser compatibility
• Fast page load speed
• SEO optimized for storage development, management, and investment keywords
• Easy in-house editing after launch
• Professional, modern, trust-driven design reflecting expertise, reliability, and innovation
________________________________________
Pages
1. HOME
Purpose: Quickly communicate who Keelbrook Vault Holdings is and why they’re the best choice for designing, building, leasing, and managing self storage facilities.
Content Highlights:
• Hero Section: Large, bold image of a modern self storage facility with headline:
"From Concept to Capacity – Your Self Storage Experts"
• Subheadline: “Keelbrook Vault Holdings delivers turnkey design, construction, leasing, and management services for profitable self storage operations.”
• Quick Service Icons:
o Facility Design & Development
o Construction & Build Management
o Lease-Up & Marketing
o Ongoing Facility Management
• Call to Action Button: “LEARN MORE” → links to ABOUT US page.
• Featured Project Highlights: Showcase a few completed or current projects with photos and stats.
• Contact Banner: “Ready to build your next self storage project? Let’s talk.” → CONTACT page.
2. ABOUT US
Purpose: Build credibility, showcase experience, and explain the value proposition.
Content Highlights:
• Who We Are: Overview of Keelbrook Vault Holdings’ history, mission, and team expertise.
• Our Approach: End-to-end process from site selection to occupancy.
• Why Choose Us:
o Industry expertise in self storage
o Proven track record in lease-up success
o Strong vendor and contractor network
3. SERVICES
Purpose: Detail all service offerings with clarity and authority.
Sections:
• Design & Development: Market analysis, site planning, and architectural design.
• Construction Management: Overseeing timelines, budgets, and quality control.
• Lease-Up Strategy: Marketing, promotions, and occupancy acceleration.
• Ongoing Facility Management: Staffing, maintenance, revenue optimization.

4. CONTACT
Purpose: Provide simple, direct ways to connect.
Content Highlights:
• Contact Form (Name, Email, Phone, Message)
• Direct Email: info@keelbrookvault.net
• Phone (if applicable)
• Google Map embed (if there’s a head office location)
• CTA: “Let’s Build Your Storage Success Story.”
Design & Technical Notes
• Visual Style: Clean, modern, bold typography, professional color palette (to be based on branding), strong imagery of self storage facilities.
• Performance: Image compression, caching, responsive scaling.
• SEO Targets: “Self storage facility developer,” “self storage construction,” “self storage management company,” “lease-up services for self storage.”

WordPress or Joomla – must be desktop and mobile friendly with fast page load speed. Need the ability to edit ourselves.

Use pantone colours - #033c5a – dark blue
#2baadf – light blue

```html
<!DOCTYPE html>
<html lang="en">
<head>
<meta charset="utf-8">
<title>Keelbrook Vault Holdings – Self Storage Experts</title>
<link rel="stylesheet" href="https://fonts.googleapis.com/css2?family=Cabin:wght@400;500;600;700&family=Lato:wght@400;700&display=swap">
<style>
:root{
  --ink:#11151f;
  --navy:#1d2436;
  --hero:#0d111c;
  --blue:#2a4fe0;
  --blue-soft:#e7ecfd;
  --brand-dark:#033c5a;
  --brand-light:#2baadf;
  --panel:#f3f4f7;
  --field:#eef0f4;
  --muted:#8a8f9c;
  --white:#ffffff;
}
*{box-sizing:border-box;margin:0;padding:0}
html,body{width:1200px;height:4219px;overflow:hidden}
body{font-family:"Lato",sans-serif;color:var(--ink);background:var(--white);position:relative}
.abs{position:absolute}
h1,h2,h3,h4,.head{font-family:"Cabin",sans-serif}
svg{display:block}

/* hero */
.hero{left:0;top:0;width:1200px;height:666px;background:linear-gradient(160deg,#141a2b 0%,#07090f 100%)}
.hero-photo{left:666px;top:0;width:534px;height:666px;background:linear-gradient(180deg,#7eaee3 0%,#c8dcf1 40%,#8d99a8 62%,#b7b9bb 100%)}
.hero-photo::after{content:"";position:absolute;inset:auto 0 0 0;height:200px;background:linear-gradient(180deg,rgba(0,0,0,0),rgba(0,0,0,.45))}
.brand{display:flex;align-items:center;gap:10px;color:var(--white)}
.brand-mark{width:34px;height:34px;border-radius:4px;background:var(--brand-light)}
.brand-name{font-family:"Cabin",sans-serif;font-weight:600;font-size:21px;line-height:1.05;color:var(--white)}
.nav a{position:absolute;top:26px;color:var(--white);font-size:12px;text-decoration:none}
.btn-ghost{left:1038px;top:25px;width:119px;height:37px;border:1px solid rgba(255,255,255,.35);background:rgba(255,255,255,.18);color:var(--white);font-size:13px;display:flex;align-items:center;justify-content:center;border-radius:2px}
.hero h1{left:67px;top:176px;width:560px;color:var(--white);font-weight:500;font-size:42px;line-height:67px}
.hero-sub{left:67px;top:326px;width:440px;color:#dfe3ec;font-size:12.5px;line-height:24px}
.btn{background:var(--blue);color:var(--white);display:flex;align-items:center;justify-content:center;gap:10px;border-radius:2px;font-size:12px}
.hero-learn{left:67px;top:424px;width:159px;height:51px}
.how{left:268px;top:440px;display:flex;align-items:center;gap:8px;color:var(--white);font-size:12px}
.stat{top:584px;width:160px;text-align:center;color:var(--white);font-family:"Cabin",sans-serif}
.stat b{display:block;font-weight:500;font-size:19px}
.stat span{font-size:15px;color:#eef}

/* quick services */
.quick{left:67px;top:764px;width:1066px;height:202px;background:var(--panel)}
.quick h2{position:absolute;top:40px;width:100%;text-align:center;font-weight:500;font-size:22px}
.qcard{top:94px;height:67px;background:var(--white);border-radius:6px;display:flex;align-items:center;gap:14px;padding:0 18px;font-size:15px;line-height:19px;font-family:"Cabin",sans-serif;font-weight:500}
.qcard svg{flex:none}

/* projects */
.sec-title{font-weight:500;font-size:28px}
.explore{left:1028px;top:1032px;display:flex;align-items:center;gap:8px;color:var(--blue);font-size:12px}
.pcard{top:1095px;width:333px;height:387px;background:var(--white);box-shadow:0 2px 14px rgba(20,30,60,.06)}
.pphoto{position:relative;height:200px;background:linear-gradient(180deg,#6fa2dd 0%,#b9cfe6 45%,#9aa3ad 70%,#6f7780 100%);overflow:hidden}
.pphoto p{position:absolute;left:6px;right:6px;bottom:4px;color:var(--white);font-size:10px;line-height:13px;text-shadow:0 1px 2px rgba(0,0,0,.5)}
.pcard h3{position:absolute;left:17px;font-weight:400;font-size:26px;color:var(--blue)}
.dim{position:absolute;left:17px;display:flex;align-items:center;gap:8px;font-size:12px}
.more{position:absolute;left:17px;color:var(--blue);font-size:13px}

.cta-text{left:67px;top:1523px;font-family:"Cabin",sans-serif;font-weight:500;font-size:26px}
.cta-btn{left:918px;top:1513px;width:192px;height:54px;font-family:"Cabin",sans-serif;font-size:24px;font-weight:500}

/* about */
.about-title{left:0;top:1628px;width:1130px;text-align:center;color:var(--blue);font-weight:500;font-size:30px}
.acard{top:1716px;height:131px;background:var(--white);border-radius:10px;box-shadow:0 2px 16px rgba(20,30,60,.07)}
.acard h4{position:absolute;left:22px;top:24px;font-family:"Lato",sans-serif;font-weight:400;font-size:15px;display:flex;align-items:center;gap:14px}
.acard h4::before{content:"";width:9px;height:9px;border-radius:50%;background:var(--blue)}
.acard p{position:absolute;left:22px;top:62px;width:340px;color:var(--muted);font-size:12px;line-height:24px}
.arrow-btn{position:absolute;right:22px;top:40px;width:67px;height:51px;border-radius:8px;background:var(--blue);display:flex;align-items:center;justify-content:center}

/* dark band */
.band{left:0;top:1886px;width:1200px;height:1192px;background:var(--navy)}
.why-title{left:84px;top:1910px;color:var(--white);font-weight:500;font-size:43px}
.wcard{top:2002px;width:324px;height:211px;background:var(--white);border:1px solid #d9dce3}
.wcard .ico{position:absolute;left:29px;top:29px;width:50px;height:50px;background:#eef0f4;display:flex;align-items:center;justify-content:center}
.wcard h3{position:absolute;left:29px;top:106px;width:262px;font-weight:500;font-size:30px;line-height:42px}

.svc-title{left:0;top:2286px;width:1212px;text-align:center;color:var(--white);font-weight:500;font-size:33px}
.svc-sub{left:0;top:2338px;width:1212px;text-align:center;color:var(--white);font-family:"Cabin",sans-serif;font-size:26px}
.svc-photo{left:185px;top:2400px;width:350px;height:498px;border-radius:22px;background:linear-gradient(180deg,#9ab8dd 0%,#dfe5ea 28%,#c9ccd0 55%,#4a4a4d 80%,#2b2a2a 100%)}
.badge{left:136px;top:2359px;width:132px;height:177px;background:var(--white);border-radius:14px;box-shadow:0 6px 20px rgba(0,0,0,.18);text-align:center}
.badge .round{width:40px;height:40px;border-radius:50%;background:var(--blue-soft);margin:18px auto 0;display:flex;align-items:center;justify-content:center}
.badge b{display:block;margin-top:20px;font-family:"Cabin",sans-serif;font-weight:500;font-size:15px}
.badge small{display:block;color:var(--muted);font-size:9px;margin-top:4px}
.avatars{display:flex;justify-content:center;margin-top:14px}
.avatars i{width:26px;height:26px;border-radius:50%;border:2px solid var(--white);margin-left:-6px;background:#b89f8b}
.avatars i:nth-child(2){background:#6b5a51}.avatars i:nth-child(3){background:#c9ad97}.avatars i:nth-child(4){background:#8d7565}.avatars i:nth-child(5){background:#d8c2b0}
.total{left:390px;top:2798px;width:185px;height:67px;background:var(--white);border-radius:14px;box-shadow:0 6px 20px rgba(0,0,0,.18);display:flex;align-items:center;gap:14px;padding:0 16px}
.total .round{width:42px;height:42px;border-radius:50%;background:var(--blue-soft);display:flex;align-items:center;justify-content:center}
.total small{display:block;color:var(--muted);font-size:9px}
.total b{font-family:"Cabin",sans-serif;font-weight:500;font-size:15px}
.svc-ico{left:686px;width:43px;height:43px;border-radius:50%;background:var(--white);display:flex;align-items:center;justify-content:center}
.svc-item{left:686px;color:var(--white)}
.svc-item h4{font-family:"Cabin",sans-serif;font-weight:500;font-size:19px}
.svc-item p{margin-top:14px;color:#8c93a5;font-size:13px}
.svc-learn{left:869px;top:2976px;width:159px;height:52px}

/* contact */
.contact-big{left:72px;top:3385px;font-family:"Cabin",sans-serif;font-weight:600;font-size:54px}
.contact-sub{left:72px;top:3470px;color:var(--blue);font-family:"Cabin",sans-serif;font-weight:500;font-size:32px}
.form{left:673px;top:3143px;width:448px;height:717px;background:var(--white);border-radius:10px;box-shadow:0 4px 24px rgba(20,30,60,.1)}
.form h2{position:absolute;left:24px;top:26px;font-weight:500;font-size:32px}
.field{position:absolute;left:23px;width:401px;background:var(--field);border-radius:20px;display:flex;align-items:center;gap:12px;padding:0 18px;font-size:12px}
.field.msg{border-radius:14px;height:93px}
.submit{position:absolute;left:23px;top:362px;width:401px;height:33px;border-radius:20px;font-size:13px}
.info{position:absolute;left:23px;display:flex;align-items:center;gap:16px;font-size:13px}
.map{position:absolute;left:23px;top:486px;width:401px;height:207px;border-radius:14px;background:linear-gradient(135deg,#eef0f3 0%,#e2e6ec 100%)}

/* footer */
.footer{left:0;top:3976px;width:1200px;height:243px;background:var(--navy);color:var(--white)}
.footer .brand{position:absolute;left:77px;top:46px}
.tagline{left:77px;top:104px;width:240px;font-size:13px;line-height:20px}
.flink{position:absolute;font-size:12px;line-height:15px}
.copy{left:77px;top:196px;font-size:12px}
.social{top:196px;width:18px;height:18px;border-radius:50%;background:var(--white)}
</style>
</head>
<body>

<!-- HERO -->
<section class="abs hero" aria-label="Hero">
  <div class="abs hero-photo" role="img" aria-label="Modern self storage facility with blue-grey cladding under a blue sky"></div>
  <div class="abs brand" style="left:18px;top:18px">
    <span class="brand-mark"></span>
    <span class="brand-name">Keelbrook Vault<br><span style="font-size:13px;font-weight:400">Holdings</span></span>
  </div>
  <nav class="nav">
    <a style="left:291px">Home</a>
    <a style="left:360px">About US</a>
    <a style="left:449px">Services</a>
    <a style="left:529px">Contact</a>
  </nav>
  <div class="abs btn-ghost">Get Started</div>
  <h1 class="abs">From Concept to Capacity – Your Self Storage Experts</h1>
  <p class="abs hero-sub">Keelbrook Vault Holdings delivers turnkey design, construction, leasing, and management services for profitable self storage operations.</p>
  <div class="abs btn hero-learn">Learn More
    <svg width="14" height="12" viewBox="0 0 14 12"><path d="M1 6h11M7 1l5 5-5 5" fill="none" stroke="#fff" stroke-width="1.6"/></svg></div>
  <div class="abs how">
    <svg width="18" height="18" viewBox="0 0 18 18"><circle cx="9" cy="9" r="8" fill="none" stroke="#fff" stroke-width="1.2"/><path d="M7 5.5v7l5.5-3.5z" fill="none" stroke="#fff" stroke-width="1.2"/></svg>
    How It Works</div>
  <div class="abs stat" style="left:673px"><b>900.000+</b><span>Properties</span></div>
  <div class="abs stat" style="left:853px"><b>9 Years</b><span>Experience</span></div>
  <div class="abs stat" style="left:1031px"><b>950K+</b><span>Happy Client</span></div>
</section>

<!-- QUICK SERVICES -->
<section class="abs quick">
  <h2>Quick Service Icons</h2>
  <div class="abs qcard" style="left:62px;width:213px">
    <svg width="18" height="18" viewBox="0 0 18 18"><path d="M2 8 9 2l7 6v8h-5v-5H7v5H2z" fill="var(--blue)"/></svg>
    <span>Facility Design &amp;<br>Development</span></div>
  <div class="abs qcard" style="left:301px;width:213px">
    <svg width="18" height="18" viewBox="0 0 18 18"><path d="M9 1 2 4v5c0 4 3 7 7 8 4-1 7-4 7-8V4z" fill="var(--blue)"/><path d="m6 9 2 2 4-4" fill="none" stroke="#fff" stroke-width="1.5"/></svg>
    <span>Construction &amp;<br>Build Management</span></div>
  <div class="abs qcard" style="left:540px;width:223px">
    <svg width="18" height="18" viewBox="0 0 18 18"><rect x="1" y="5" width="16" height="11" rx="2" fill="var(--blue)"/><path d="M6 5V3h6v2" fill="none" stroke="var(--blue)" stroke-width="1.6"/><path d="M1 10h16" stroke="#fff"/></svg>
    <span>Lease-Up &amp; Marketing</span></div>
  <div class="abs qcard" style="left:789px;width:213px">
    <svg width="18" height="18" viewBox="0 0 18 18"><rect x="1" y="3" width="16" height="13" rx="2" fill="var(--blue)"/><rect x="10" y="8" width="7" height="4" fill="#fff"/></svg>
    <span>Ongoing Facility<br>Management</span></div>
</section>

<!-- FEATURED PROJECTS -->
<h2 class="abs sec-title" style="left:77px;top:1038px">Featured Project Highlights</h2>
<div class="abs explore">Explore All
  <svg width="14" height="12" viewBox="0 0 14 12"><path d="M1 6h11M7 1l5 5-5 5" fill="none" stroke="var(--blue)" stroke-width="1.6"/></svg></div>

<article class="abs pcard" style="left:67px">
  <div class="pphoto" role="img" aria-label="Large industrial storage building with loading bays under a clear sky">
    <p>The exterior is spacious and sturdy, built to accommodate a wide variety of goods in large quantities. The building's structure typically includes tall storage racks, wide loading and unloading areas, and optimal lighting systems to support logistics and distribution operations.</p>
  </div>
  <h3 style="top:225px">Southside Storage</h3>
  <div class="dim" style="top:296px"><svg width="14" height="14" viewBox="0 0 14 14"><path d="M1 5V1h4M9 1h4v4M13 9v4H9M5 13H1V9" fill="none" stroke="#111" stroke-width="1.6"/></svg>25x25 m</div>
  <a class="more" style="top:343px">View Details</a>
</article>

<article class="abs pcard" style="left:434px">
  <div class="pphoto" role="img" aria-label="Warehouse complex with a small construction vehicle parked in front">
    <p>In the center, a small construction vehicle is parked on the ground, suggesting some site preparation or maintenance activity. The structure is spacious, designed for efficient logistics, storage, and industrial operations, with ample space for vehicles and equipment to move around. The clear blue sky above adds to the bright and clean industrial setting.</p>
  </div>
  <h3 style="top:222px">Northest Storage</h3>
  <div class="dim" style="top:288px"><svg width="14" height="14" viewBox="0 0 14 14"><path d="M1 5V1h4M9 1h4v4M13 9v4H9M5 13H1V9" fill="none" stroke="#111" stroke-width="1.6"/></svg>15x15 m</div>
  <a class="more" style="top:338px">View Details</a>
</article>

<article class="abs pcard" style="left:800px">
  <div class="pphoto" role="img" aria-label="Industrial park buildings with a construction crane in the background">
    <p>In the background, a construction crane suggests expansion or new buildings being erected. The surrounding area is clean and organized, with patches of grass and small landscaped sections along the road. The overall impression is of a well-planned, contemporary industrial park designed for manufacturing, storage, or logistics operations.</p>
  </div>
  <h3 style="top:213px">Industrial Storage</h3>
  <div class="dim" style="top:288px"><svg width="14" height="14" viewBox="0 0 14 14"><path d="M1 5V1h4M9 1h4v4M13 9v4H9M5 13H1V9" fill="none" stroke="#111" stroke-width="1.6"/></svg>60x60 m</div>
  <a class="more" style="top:343px">View Details</a>
</article>

<p class="abs cta-text">Ready to build your next self storage project? Let’s talk.</p>
<div class="abs btn cta-btn">Contact</div>

<!-- ABOUT -->
<h2 class="abs about-title">+ About Us</h2>
<article class="abs acard" style="left:92px;width:491px">
  <h4>Who We Are</h4>
  <p>Overview Of Keelbrook Vault Holdings’ History, Mission, And Team Expertise.</p>
  <div class="arrow-btn"><svg width="22" height="18" viewBox="0 0 22 18"><path d="m3 3 6 6-6 6M11 3l6 6-6 6" fill="none" stroke="#fff" stroke-width="2"/></svg></div>
</article>
<article class="abs acard" style="left:616px;width:492px">
  <h4>Our Approach</h4>
  <p>End-To-End Process From Site Selection To Occupancy.</p>
  <div class="arrow-btn"><svg width="22" height="18" viewBox="0 0 22 18"><path d="m3 3 6 6-6 6M11 3l6 6-6 6" fill="none" stroke="#fff" stroke-width="2"/></svg></div>
</article>

<!-- WHY CHOOSE US + SERVICES -->
<section class="abs band"></section>
<h2 class="abs why-title">Why Choose Us</h2>
<article class="abs wcard" style="left:84px">
  <div class="ico"><svg width="18" height="20" viewBox="0 0 18 20"><rect x="2" y="9" width="14" height="10" rx="2" fill="none" stroke="#333" stroke-width="1.6"/><path d="M5 9V6a4 4 0 0 1 8 0v3" fill="none" stroke="#333" stroke-width="1.6"/></svg></div>
  <h3>Industry expertise in self storage</h3></article>
<article class="abs wcard" style="left:442px">
  <div class="ico"><svg width="18" height="20" viewBox="0 0 18 20"><path d="M9 1 2 4v5c0 5 3 8 7 10 4-2 7-5 7-10V4z" fill="none" stroke="#333" stroke-width="1.6"/><circle cx="9" cy="9" r="2.5" fill="#333"/></svg></div>
  <h3>Proven track record in lease-up success</h3></article>
<article class="abs wcard" style="left:802px">
  <div class="ico"><svg width="20" height="20" viewBox="0 0 20 20"><circle cx="10" cy="10" r="8" fill="none" stroke="#333" stroke-width="1.6"/><ellipse cx="10" cy="10" rx="3.5" ry="8" fill="none" stroke="#333" stroke-width="1.4"/><path d="M2 10h16" stroke="#333" stroke-width="1.4"/></svg></div>
  <h3>Strong vendor and contractor network</h3></article>

<h2 class="abs svc-title">Service</h2>
<p class="abs svc-sub">Detail All Service Offerings With Clarity And Authority.</p>

<div class="abs svc-photo" role="img" aria-label="Modern two-storey storage building with white panels and dark windows"></div>
<div class="abs badge">
  <div class="round"><svg width="22" height="16" viewBox="0 0 22 16"><circle cx="11" cy="4" r="3" fill="var(--blue)"/><circle cx="4" cy="6" r="2.4" fill="var(--blue)"/><circle cx="18" cy="6" r="2.4" fill="var(--blue)"/><path d="M5 15a6 6 0 0 1 12 0zM0 15a4 4 0 0 1 6-3.5M22 15a4 4 0 0 0-6-3.5" fill="var(--blue)"/></svg></div>
  <b>950K+</b><small>Happy Client</small>
  <div class="avatars" aria-label="Client avatars"><i style="margin-left:0"></i><i></i><i></i><i></i><i></i></div>
</div>
<div class="abs total">
  <div class="round"><svg width="14" height="18" viewBox="0 0 14 18"><path d="M7 1a6 6 0 0 0-6 6c0 4 6 10 6 10s6-6 6-10a6 6 0 0 0-6-6z" fill="var(--blue)"/><circle cx="7" cy="7" r="2.2" fill="#fff"/></svg></div>
  <div><small>Total Property</small><b>900K+ Units</b></div>
</div>

<div class="abs svc-ico" style="top:2385px"><svg width="18" height="18" viewBox="0 0 18 18"><path d="M2 8 9 2l7 6v8h-5v-5H7v5H2z" fill="var(--blue)"/></svg></div>
<div class="abs svc-item" style="top:2449px"><h4>Facility Design &amp; Development</h4><p>Market analysis, site planning, and architectural design.</p></div>
<div class="abs svc-ico" style="top:2520px"><svg width="18" height="18" viewBox="0 0 18 18"><path d="M9 1 2 4v5c0 4 3 7 7 8 4-1 7-4 7-8V4z" fill="var(--blue)"/><path d="m6 9 2 2 4-4" fill="none" stroke="#fff" stroke-width="1.5"/></svg></div>
<div class="abs svc-item" style="top:2583px"><h4>Construction Management</h4><p>Overseeing timelines, budgets, and quality control.</p></div>
<div class="abs svc-ico" style="top:2662px"><svg width="18" height="18" viewBox="0 0 18 18"><rect x="1" y="5" width="16" height="11" rx="2" fill="var(--blue)"/><path d="M6 5V3h6v2" fill="none" stroke="var(--blue)" stroke-width="1.6"/><path d="M1 10h16" stroke="#fff"/></svg></div>
<div class="abs svc-item" style="top:2725px"><h4>Lease-Up Strategy</h4><p>Marketing, promotions, and occupancy acceleration.</p></div>
<div class="abs svc-ico" style="top:2813px;left:683px"><svg width="18" height="18" viewBox="0 0 18 18"><rect x="1" y="3" width="16" height="13" rx="2" fill="var(--blue)"/><rect x="10" y="8" width="7" height="4" fill="#fff"/></svg></div>
<div class="abs svc-item" style="top:2876px;left:683px"><h4>Ongoing Facility Management</h4><p>Staffing, maintenance, revenue optimization.</p></div>
<div class="abs btn svc-learn">Learn More
  <svg width="14" height="12" viewBox="0 0 14 12"><path d="M1 6h11M7 1l5 5-5 5" fill="none" stroke="#fff" stroke-width="1.6"/></svg></div>

<!-- CONTACT -->
<h2 class="abs contact-big">CONTACT</h2>
<p class="abs contact-sub">Provide simple, direct ways to connect.</p>
<form class="abs form">
  <h2>Contact</h2>
  <div class="field" style="top:82px;height:38px"><svg width="14" height="14" viewBox="0 0 14 14"><circle cx="7" cy="4" r="3.2" fill="var(--blue)"/><path d="M1 14a6 6 0 0 1 12 0z" fill="var(--blue)"/></svg>Name</div>
  <div class="field" style="top:139px;height:38px"><svg width="14" height="12" viewBox="0 0 14 12"><rect y="1" width="14" height="10" rx="1.5" fill="var(--blue)"/><path d="m1 2 6 5 6-5" fill="none" stroke="#fff" stroke-width="1.2"/></svg>Email</div>
  <div class="field" style="top:196px;height:37px"><svg width="14" height="14" viewBox="0 0 14 14"><path d="M3 1 5.5 4 4 6a8 8 0 0 0 4 4l2-1.5 3 2.5-1.5 2C6 13 1 8 1 2.5z" fill="var(--blue)"/></svg>Phone</div>
  <div class="field msg" style="top:251px"><svg width="14" height="14" viewBox="0 0 14 14"><rect x="1" y="2" width="10" height="11" rx="1" fill="none" stroke="var(--blue)" stroke-width="1.4"/><path d="m6 9 1-3 6-6 2 2-6 6z" fill="var(--blue)"/></svg>Message</div>
  <div class="btn submit">Submit</div>
  <div class="info" style="top:414px"><svg width="16" height="12" viewBox="0 0 16 12"><rect width="16" height="12" rx="1.5" fill="var(--blue)"/><path d="m1 1 7 6 7-6" fill="none" stroke="#fff" stroke-width="1.2"/></svg>info@keelbrookvault.net</div>
  <div class="info" style="top:449px;color:var(--muted);font-size:12px"><svg width="15" height="15" viewBox="0 0 14 14"><path d="M3 1 5.5 4 4 6a8 8 0 0 0 4 4l2-1.5 3 2.5-1.5 2C6 13 1 8 1 2.5z" fill="var(--blue)"/></svg>Phone Number</div>
  <div class="map" role="img" aria-label="Street map showing the head office location"></div>
</form>

<!-- FOOTER -->
<footer class="abs footer">
  <div class="brand">
    <span class="brand-mark"></span>
    <span class="brand-name" style="font-size:25px">Keelbrook Vault<br><span style="font-size:15px;font-weight:400">Holdings</span></span>
  </div>
  <p class="abs tagline">from concept to capacity - yourself storage express</p>
  <a class="flink" style="left:393px;top:48px">Home</a>
  <a class="flink" style="left:393px;top:81px">Project Highlights</a>
  <a class="flink" style="left:393px;top:107px">Quick Service</a>
  <a class="flink" style="left:393px;top:136px">Why Choose Us</a>
  <a class="flink" style="left:539px;top:48px">About Us</a>
  <a class="flink" style="left:541px;top:82px">Services</a>
  <a class="flink" style="left:541px;top:107px">Privacy Policy</a>
  <a class="flink" style="left:735px;top:48px">Services</a>
  <a class="flink" style="left:731px;top:80px">Term and<br>condition</a>
  <a class="flink" style="left:833px;top:48px">Contact Us</a>
  <a class="flink" style="left:833px;top:88px">Privacy Policy</a>
  <p class="abs copy">Copyright © 2025 Keelbrook Vault Holdings &nbsp;All Rights Reserved.</p>
  <span class="abs social" style="left:994px"></span>
  <span class="abs social" style="left:1030px"></span>
  <span class="abs social" style="left:1066px"></span>
  <span class="abs social" style="left:1103px"></span>
</footer>

</body>
</html>
```